Package/Product Design: Fullora 100% Scalp Coverage Powders

Need to design "high style" box and product disc design. Open to any and all suggestions. We sell 800+ skus a month on Marketvale and looking to take our box design to the next level so that we can sell even more with new look. Our competition is https://www.brevano.com/ and https://www.quillsy.com/ I know Brevano has a ton of money,,, but their products look "high touch, high style" and that is what we are going after. The compact has to have the ingredients on the back, same as the box. So looking for a design that makes the packaging look sleek, and still gets out point across. Logo should be in White or Black.

Target Market(s)

We sell to individuals who are experiencing hair loss, thinning hair, or gray/balding hair. This product creates the illusion of hair and allows clients get gain back confidence.

We sell on Marketvale (search fullora or scalp concealer), and www.fullorahairdust.com

Industry/Entity Type

Hair And Beauty

Logo Text

Fullora 100% Scalp Coverage Powders

Colors

Designer to choose colors to be used in the design.

Requirements
Must have
• Quality/high touch/high feel look to the packaging. Open to any and all suggestions.

```html
<!DOCTYPE html>
<html lang="en">
<head>
<meta charset="utf-8">
<title>Fullora Hair Powder – Box and Compact Packaging</title>
<link rel="stylesheet" href="https://fonts.googleapis.com/css2?family=Roboto:wght@400;500;700&family=Roboto+Condensed:wght@400&display=swap">
<style>
  :root {
    --backdrop: #b3b3b3;
    --carton: #231f20;
    --white: #ffffff;
    --ink: #231f20;
    --rule: #9a9a9a;
    --blue: #0b78c2;
    --purple: #7d2d94;
    --orange: #f59a2a;
  }
  html, body {
    margin: 0;
    padding: 0;
    width: 1200px;
    height: 1200px;
    overflow: hidden;
    background: var(--backdrop);
  }
  .artboard {
    display: block;
    width: 1200px;
    height: 1200px;
    font-family: "Roboto", Arial, sans-serif;
  }
  .carton { fill: var(--carton); }
  .label-white { fill: var(--white); }
  .label-ink { fill: var(--ink); }
  .brand-name {
    font-family: "Roboto Condensed", "Roboto", sans-serif;
    font-weight: 400;
    letter-spacing: 1.5px;
    fill: var(--white);
  }
  .copy-sm { font-size: 8.5px; }
  .copy-xs { font-size: 7.2px; }
  .panel-copy { font-size: 10.2px; fill: var(--white); }
  .panel-head { font-weight: 700; }
  .panel-tagline { font-size: 15px; fill: var(--white); }
  .stop-blue { stop-color: var(--blue); }
  .stop-purple { stop-color: var(--purple); }
  .stop-orange { stop-color: var(--orange); }
</style>
</head>
<body>
<svg class="artboard" viewBox="0 0 1000 1000" xmlns="http://www.w3.org/2000/svg">
  <defs>
    <linearGradient id="spectrum-h" x1="0" y1="0" x2="1" y2="0">
      <stop offset="0.12" class="stop-blue"/>
      <stop offset="0.5" class="stop-purple"/>
      <stop offset="0.92" class="stop-orange"/>
    </linearGradient>
    <linearGradient id="spectrum-v" x1="0" y1="1" x2="0" y2="0">
      <stop offset="0.12" class="stop-blue"/>
      <stop offset="0.5" class="stop-purple"/>
      <stop offset="0.95" class="stop-orange"/>
    </linearGradient>
    <clipPath id="lid-lower"><rect x="60" y="815" width="330" height="200"/></clipPath>
  </defs>

  <!-- Box dieline -->
  <g class="box-dieline">
    <polygon class="carton" points="300,97 345,12 388,12 432,97"/>
    <polygon class="carton" points="300,460 432,460 388,545 345,545"/>
    <polygon class="carton" points="815,97 860,12 920,12 965,97"/>
    <polygon class="carton" points="815,460 965,460 920,545 860,545"/>
    <polygon class="carton" points="195,112 297,97 297,460 195,450"/>
    <rect class="carton" x="296" y="97" width="150" height="363"/>
    <rect class="carton" x="440" y="95" width="370" height="365"/>
    <rect class="carton" x="455" y="459" width="355" height="161"/>
    <polygon class="carton" points="809,97 970,97 970,460 809,460"/>

    <!-- Left side panel: directions -->
    <rect class="side-panel" x="297" y="105" width="135" height="345" fill="url(#spectrum-v)"/>
    <g class="directions" transform="translate(427,108) rotate(90)">
      <text class="panel-copy"><tspan class="panel-head" x="0" y="9">Directions:</tspan>
        <tspan x="0" y="22">In a circular motion, rub applicator brush around the</tspan>
        <tspan x="0" y="35">pressed powder. Lightly apply to desired area directly on</tspan>
        <tspan x="0" y="48">the scalp using small round strokes. Repeat until proper</tspan>
        <tspan x="0" y="61">coverage is obtained.</tspan></text>
      <text class="panel-tagline" x="76" y="100">Talc-Free  |  Hair Powder</text>
    </g>

    <!-- Right side panel: ingredients -->
    <rect class="side-panel" x="822" y="105" width="136" height="345" fill="url(#spectrum-v)"/>
    <g class="ingredients" transform="translate(830,448) rotate(-90)">
      <text class="panel-copy"><tspan class="panel-head" x="0" y="10">Ingredients:</tspan>
        <tspan x="0" y="22">Mica, Kaolin, Octyldodecyl Stearoyl Stearate, Synthetic Wax,</tspan>
        <tspan x="0" y="34">Ethylhexyl Palmitate, Bis-Diglyceryl Polyacyladipate-2, Tocopheryl</tspan>
        <tspan x="0" y="46">Acetate, Phenoxyethanol, Methylparaben, Propylparaben, Caprylyl</tspan>
        <tspan x="0" y="58">Glycol, Ethylhexylglycerin, CI 77891, CI 77492, CI 77499,</tspan>
        <tspan x="0" y="70">CI 77491</tspan>
        <tspan x="0" y="82">LOT: 12122013-01</tspan></text>
    </g>

    <!-- Front panel -->
    <text class="label-white copy-sm" text-anchor="middle" x="632" y="130">100%</text>
    <text class="label-white copy-sm" text-anchor="middle" x="632" y="142">SCALP COVERAGE</text>
    <rect class="front-banner" x="455" y="200" width="355" height="157" fill="url(#spectrum-h)"/>
    <text class="brand-name" text-anchor="middle" x="632" y="287" font-size="30">FULLORA</text>
    <text class="label-white copy-sm" text-anchor="middle" x="630" y="404">TALC- FREE | HAIR POWDER</text>
    <text class="label-white copy-sm" text-anchor="middle" x="630" y="427">NET WT. 32oz / 9g</text>
  </g>

  <!-- Compact lid -->
  <g class="compact-lid">
    <circle class="carton" cx="222" cy="812" r="151"/>
    <circle cx="222" cy="812" r="143" fill="url(#spectrum-h)"/>
    <g clip-path="url(#lid-lower)">
      <circle class="carton" cx="222" cy="812" r="143"/>
    </g>
    <circle cx="222" cy="812" r="142" fill="none" stroke="url(#spectrum-h)" stroke-width="2.2"/>
    <circle class="carton" cx="222" cy="812" r="82"/>
    <circle cx="222" cy="812" r="76" fill="url(#spectrum-h)"/>
    <g clip-path="url(#lid-lower)">
      <circle class="carton" cx="222" cy="812" r="77"/>
    </g>
    <text class="label-white copy-sm" text-anchor="middle" x="218" y="692">100%</text>
    <text class="label-white copy-sm" text-anchor="middle" x="218" y="704">SCALP COVERAGE</text>
    <text class="brand-name" text-anchor="middle" x="222" y="806" font-size="17">FULLORA</text>
    <text class="label-white copy-sm" text-anchor="middle" x="218" y="911">TALC- FREE | HAIR POWDER</text>
    <text class="label-white copy-sm" text-anchor="middle" x="218" y="932">NET WT. 32oz / 9g</text>
  </g>

  <!-- Compact base label -->
  <g class="compact-base">
    <circle cx="557" cy="812" r="151" fill="url(#spectrum-h)"/>
    <circle class="label-white" cx="557" cy="812" r="136" stroke="var(--rule)" stroke-width="0.8"/>
    <text class="label-ink copy-xs" text-anchor="middle">
      <tspan x="557" y="715"><tspan font-weight="700">Ingredients:</tspan> Mica,</tspan>
      <tspan x="557" y="726">Kaolin, Octyldodecyl Stearoyl</tspan>
      <tspan x="557" y="737">Stearate, Synthetic Wax, Ethylhexyl</tspan>
      <tspan x="557" y="748">Palmitate, Bis-Diglyceryl</tspan>
      <tspan x="557" y="759">Polyacyladipate-2, Tocopheryl Acetate,</tspan>
      <tspan x="557" y="770">Phenoxyethanol, Methylparaben,</tspan>
      <tspan x="557" y="781">Propylparaben, Caprylyl Glycol, Ethylhexylglycerin,</tspan>
      <tspan x="557" y="792">CI 77891, CI 77492, CI 77499, CI 77491</tspan>
      <tspan x="557" y="806"><tspan font-weight="700">WARNING:</tspan> Keep out of eyes. Stop use if irritation</tspan>
      <tspan x="557" y="817">occurs. Keep out of reach of children.</tspan>
    </text>
    <text class="label-ink" font-size="5.5" text-anchor="middle" x="560" y="829">Distributed by:</text>
    <g class="pao-icon" fill="none" stroke="var(--ink)" stroke-width="0.9">
      <path d="M466,841 L470,833 L497,833 L501,841"/>
      <rect x="466" y="841" width="35" height="18"/>
    </g>
    <text class="label-ink" font-size="7" text-anchor="middle" x="483.5" y="853">24M</text>
    <text class="label-ink copy-xs" x="514">
      <tspan x="514" y="840" font-weight="700">Fullora Hair Powder</tspan>
      <tspan x="514" y="850">4120 Harbor Ln STE 210</tspan>
      <tspan x="514" y="860">Palm Grove, FL 33910</tspan>
      <tspan x="494" y="870" font-weight="700" font-size="6.4">www.fullorahairdust.com</tspan>
    </text>
    <text class="label-ink" font-size="10.5" text-anchor="middle" x="555" y="891">Color: Dark Brown</text>
    <text class="label-ink copy-sm" text-anchor="middle" x="555" y="906">Made in P.R.C.</text>
  </g>

  <!-- Standalone wordmark -->
  <text class="brand-name" text-anchor="middle" x="868" y="848" font-size="30">FULLORA</text>
</svg>
</body>
</html>
```